Design a business card for Brenton's Heat Guardian
Brenton's Heat Guardian
Design a business card for Brenton's Heat Guardian - Food
Creative Brief
Traditional
Hal Brenton
President and CEO
52894 Corvane Lane Clinton Township, MI 48052
hbrenton1947@mailvex.example
www.brentonsheatguardian.example
Simple color marks, with some white space to write notes

```html
<!DOCTYPE html>
<html lang="en">
<head>
<meta charset="utf-8">
<title>Brenton's Heat Guardian — Business Card</title>
<link rel="stylesheet" href="https://fonts.googleapis.com/css2?family=Roboto+Condensed:wght@400;700&display=swap">
<style>
  :root {
    --backdrop: #8a8a8a;
    --card-white: #ffffff;
    --ink: #1c1c1c;
    --band-black: #1e1e1e;
    --accent-orange: #f28a1a;
    --accent-red: #e0461c;
    --text-light: #ffffff;
    --text-body: #2a2a2a;
  }
  * { box-sizing: border-box; margin: 0; padding: 0; }
  html, body {
    width: 1200px; height: 908px; overflow: hidden;
    background: var(--backdrop);
    font-family: "Roboto Condensed", Arial, sans-serif;
  }
  .stage { position: relative; width: 1200px; height: 908px; }
  .card {
    position: absolute; width: 540px; height: 320px;
    background: var(--card-white); border-radius: 18px; overflow: hidden;
    box-shadow: 0 10px 28px rgba(0,0,0,.28);
  }
  .card--back { left: 70px; top: 110px; }
  .card--front { left: 590px; top: 478px; }

  .wordmark {
    font-weight: 700; color: var(--ink); line-height: 1.05;
  }
  .card--back .wordmark {
    position: absolute; left: 34px; bottom: 36px; font-size: 30px;
  }
  .card--front .wordmark {
    position: absolute; left: 34px; top: 96px; font-size: 30px; width: 220px;
  }

  .band { position: absolute; inset: 0; width: 540px; height: 320px; }

  .person {
    position: absolute; right: 34px; top: 130px; text-align: right;
    color: var(--text-light);
  }
  .person__name { font-size: 20px; font-weight: 400; }
  .person__title { font-size: 17px; margin-top: 4px; }

  .contact {
    position: absolute; left: 34px; top: 188px; font-size: 12.5px;
    color: var(--text-body); line-height: 1.3;
  }
  .contact__address { margin-bottom: 6px; }
  .contact__row { display: flex; align-items: center; gap: 6px; margin-top: 3px; }
  .contact__icon {
    width: 14px; height: 14px; border-radius: 50%;
    background: var(--accent-orange); flex: none;
    display: flex; align-items: center; justify-content: center;
  }
</style>
</head>
<body>
<main class="stage">

  <section class="card card--back" aria-label="Card back">
    <p class="wordmark">Brenton's Heat Guardian</p>
  </section>

  <section class="card card--front" aria-label="Card front">
    <svg class="band" viewBox="0 0 540 320" aria-hidden="true">
      <defs>
        <linearGradient id="accentGrad" x1="0" y1="0" x2="0" y2="1">
          <stop offset="0" stop-color="var(--accent-orange)"/>
          <stop offset="1" stop-color="var(--accent-red)"/>
        </linearGradient>
      </defs>
      <path d="M240 0 C330 80 365 200 398 320 H420 C385 200 350 80 262 0 Z" fill="url(#accentGrad)"/>
      <path d="M262 0 H540 V320 H420 C385 200 350 80 262 0 Z" fill="var(--band-black)"/>
    </svg>

    <p class="wordmark">Brenton's Heat Guardian</p>

    <div class="person">
      <p class="person__name">Hal Brenton</p>
      <p class="person__title">President and CEO</p>
    </div>

    <address class="contact" style="font-style:normal">
      <p class="contact__address">52894 Corvane Lane<br>Clinton Township, MI 48052</p>
      <p class="contact__row">
        <span class="contact__icon"><svg width="8" height="8" viewBox="0 0 10 10"><path d="M2 1 L4 1 L4.6 3 L3.5 3.8 Q4.5 5.8 6.2 6.5 L7 5.4 L9 6 L9 8 Q5 9 1.5 4.5 Q1 2.5 2 1 Z" fill="#fff"/></svg></span>586-555-0142
      </p>
      <p class="contact__row">
        <span class="contact__icon"><svg width="8" height="8" viewBox="0 0 10 10"><path d="M2 1 L4 1 L4.6 3 L3.5 3.8 Q4.5 5.8 6.2 6.5 L7 5.4 L9 6 L9 8 Q5 9 1.5 4.5 Q1 2.5 2 1 Z" fill="#fff"/></svg></span>248-555-0187
      </p>
      <p class="contact__row">
        <span class="contact__icon"><svg width="8" height="8" viewBox="0 0 10 10"><rect x="1" y="2.5" width="8" height="5.5" fill="none" stroke="#fff" stroke-width="1.2"/><path d="M1 2.5 L5 5.5 L9 2.5" fill="none" stroke="#fff" stroke-width="1.2"/></svg></span>hbrenton1947@mailvex.example
      </p>
      <p class="contact__row">
        <span class="contact__icon"><svg width="8" height="8" viewBox="0 0 10 10"><circle cx="5" cy="5" r="3.8" fill="none" stroke="#fff" stroke-width="1.1"/><path d="M1.2 5 H8.8 M5 1.2 Q2.8 5 5 8.8 M5 1.2 Q7.2 5 5 8.8" fill="none" stroke="#fff" stroke-width=".9"/></svg></span>www.brentonsheatguardian.example
      </p>
    </address>
  </section>

</main>
</body>
</html>
```